Newsletter-Design für Online-Versandhandel
Zielgruppe
Wir sind ein online Versand Handel mit dem Schwerpunkt auf Bio Bettwaren. Unsere Zielgruppe sind ökologisch bewusste Menschen mittleren bis höheren Alters.
Aufgabenstellung
Unsere Corporate Farbe ist vornehmlich ein sanftes Grün.
www.laubhaus-wendorf.example
Hier eine Auswahl von Newslettern
http://newsletter.moosgarten.example/u/gm.php?prm=4pTbQkAzzR_519384026_7730512_41826
http://newslink.pulvamoda.example/u/gm.php?prm=rYt58bkw2L_927150384_3649281_20573
Bisher haben wir unsere NL als kleinen, persönlichen Text gestaltet und dazu zwei oder drei Teaser.
Den Text möchte ich beibehalten und neben meiner Unterschrift ein ein kleines persönliches Bild einfügen.
Wichtig! Wir versenden mit mailchimp, wir benötigen eine dafür kompatible Vorlage.

```html
<!DOCTYPE html>
<html lang="de">
<head>
<meta charset="utf-8">
<title>Wendorf Naturversand Newsletter</title>
<link href="https://fonts.googleapis.com/css2?family=Tinos:wght@400;700&display=swap" rel="stylesheet">
<style>
:root{
  --green-dark:#00964a;
  --green-card:#5aad4a;
  --green-teaser:#3bb36b;
  --green-text:#4aa845;
  --grey-btn:#666666;
  --grey-text:#6e6e6e;
  --page-bg:#f3f3f3;
  --rug-bg:#eeeeea;
  --black:#000000;
  --white:#ffffff;
}
*{margin:0;padding:0;box-sizing:border-box}
html,body{width:1200px;height:4063px;overflow:hidden}
body{background:var(--page-bg);font-family:"Tinos",serif;position:relative}
.sheet{position:absolute;left:129px;top:84px;width:910px;height:3805px;background:var(--white)}
.abs{position:absolute}
.topbar{left:0;top:0;width:910px;height:34px;background:var(--green-dark);color:var(--white);font-weight:700;font-size:17px;display:flex;justify-content:space-between;align-items:center;padding:0 2px 0 4px}
.topbar span{display:flex;align-items:center;gap:8px}
.brand{left:0;width:910px;text-align:center;color:var(--green-dark)}
.brand-name{font-size:52px;font-weight:700;display:flex;justify-content:center;align-items:center;gap:14px;line-height:60px}
.brand-name i{display:inline-block;width:40px;height:40px;border-radius:50%;background:var(--green-dark)}
.brand-sub{font-size:24px;letter-spacing:3px;margin-top:2px}
.rule{left:19px;top:176px;width:872px;height:1px;background:#cfcfcf}
.tagline{left:0;top:200px;width:910px;text-align:center;font-size:20px;color:#333;letter-spacing:.5px}
.photo{display:block}
.hero{left:0;top:249px;width:910px;height:366px;background:linear-gradient(180deg,#8a8a88 0%,#c9c3bd 55%,#d9a9a9 100%)}
.diamond{left:59px;top:265px;width:160px;height:160px;background:var(--green-dark);transform:rotate(45deg)}
.diamond-text{left:59px;top:310px;width:160px;text-align:center;color:var(--white);font-size:34px;line-height:37px}
.welcome{left:0;top:685px;width:910px;text-align:center;font-size:22px;font-weight:700;color:#3a3a3a}
.intro{left:0;top:730px;width:910px;text-align:center;font-size:16.5px;font-weight:700;line-height:33px;color:var(--grey-text)}
.btn{background:var(--grey-btn);color:var(--white);font-size:24px;font-weight:700;display:flex;align-items:center;justify-content:center}
.card{width:274px;height:426px;background:var(--green-card);border-radius:10px;text-align:center}
.card .photo{position:absolute;left:17px;top:20px;width:240px;height:225px}
.card h3{position:absolute;top:256px;width:100%;font-size:18px;font-weight:400;color:#173b12;white-space:nowrap}
.card p{position:absolute;top:282px;left:0;right:0;font-size:14.5px;font-weight:700;line-height:26px;color:var(--white);white-space:nowrap}
.card .price{position:absolute;top:392px;width:100%;font-size:21px;font-weight:700;color:var(--white)}
.banner{left:0;top:2034px;width:910px;height:318px;background:linear-gradient(180deg,#c7bcae 0%,#b59a7e 50%,#d8cdbd 100%)}
.banner-label{left:268px;top:2162px;width:377px;height:60px;background:var(--green-card);color:var(--white);font-size:37px;display:flex;align-items:center;justify-content:center}
.rug{width:437px;height:411px;background:var(--rug-bg);border:1px solid #d6d6d0}
.rug .photo{position:absolute;left:9px;top:8px;width:419px;height:276px}
.rug .price{position:absolute;left:124px;top:284px;width:188px;height:63px;background:var(--green-card);color:var(--white);font-size:27px;display:flex;align-items:center;justify-content:center}
.rug h3{position:absolute;top:362px;width:100%;text-align:center;font-size:27px;font-weight:400;color:var(--green-text)}
.teaser{left:78px;width:756px;height:319px;border:3px solid var(--green-teaser)}
.teaser .photo{position:absolute;left:16px;top:19px;width:282px;height:274px}
.teaser h3{position:absolute;left:355px;top:30px;font-size:26px;font-weight:400;color:var(--green-text)}
.teaser p{position:absolute;left:355px;top:78px;width:380px;font-size:17px;line-height:35px;color:var(--grey-text);white-space:nowrap}
.teaser .price{position:absolute;left:433px;top:243px;width:152px;height:40px;background:var(--green-teaser);color:var(--white);font-size:23px;display:flex;align-items:center;justify-content:center}
.footer{left:0;top:3576px;width:910px;height:229px;background:var(--black)}
.footer .brand{top:28px;color:var(--green-dark)}
.footer .brand-name{font-size:44px;line-height:52px}
.footer .brand-name i{width:32px;height:32px}
.social{left:0;top:160px;width:910px;display:flex;justify-content:center;gap:14px}
.social span{width:36px;height:36px;border-radius:6px;background:#d8232a}
.social span.blue{background:#2c4d9c}
</style>
</head>
<body>
<div class="sheet">
  <div class="abs topbar">
    <span><svg width="20" height="15" viewBox="0 0 20 15"><rect x="1" y="1" width="18" height="13" fill="none" stroke="#fff" stroke-width="2"/><path d="M1 1 L10 8 L19 1" fill="none" stroke="#fff" stroke-width="2"/></svg>info@laubhaus-wendorf.example</span>
    <span><svg width="16" height="16" viewBox="0 0 24 24"><path fill="#fff" d="M6.6 10.8a15 15 0 006.6 6.6l2.2-2.2c.3-.3.7-.4 1-.2 1.1.4 2.3.6 3.6.6.6 0 1 .4 1 1V20c0 .6-.4 1-1 1C10.6 21 3 13.4 3 4c0-.6.4-1 1-1h3.5c.6 0 1 .4 1 1 0 1.3.2 2.5.6 3.6.1.3 0 .7-.2 1z"/></svg>07541 902 3378</span>
  </div>

  <div class="abs brand" style="top:56px">
    <div class="brand-name"><i></i>Wendorf</div>
    <div class="brand-sub">NATURVERSAND-ONLINESHOP</div>
  </div>
  <div class="abs rule"></div>
  <div class="abs tagline">FÜR BETTWAREN, TEPPICHE UND ALLERGIEPRODUKTE</div>

  <div class="abs hero photo" role="img" aria-label="Schlafzimmer mit Bett, rosa Kissen und Sessel"></div>
  <div class="abs diamond"></div>
  <div class="abs diamond-text">Einfach<br>geschenk</div>

  <h1 class="abs welcome">Herzlich Willkommen bei Wendorf Naturversand!</h1>
  <p class="abs intro">Kaufen Sie bei uns hochwertige, ökologische Produkte für natürliches Wohnen und gesundes Schlafen<br>Handwebteppiche, Produkte zum Schutz vor Elektrosmog, orthopädische Kissen, Allergiker Bettdecken<br>Kirschkernkissen, Nackenwärmer, Daunenkissen, Kaschmirdecken. Liegen Sie gesund und richtig in<br>auf unseren Naturlatexmatratzen und unseren Bio Lattenrosten. Kuscheln Sie sich in unsere ökologischen<br>Bettwaren aus kbA Baumwolle mit den verschiedensten Füllungen.</p>
  <div class="abs btn" style="left:287px;top:916px;width:339px;height:50px">Weitere Informationen</div>

  <div class="abs card" style="left:2px;top:1010px"><div class="photo" role="img" aria-label="Person schläft auf weißem Kissen" style="background:linear-gradient(160deg,#f4f4f4,#c9c2bd)"></div><h3>Daunen Ganzjahresdecke</h3><p>Bio Ganzjahresdecke Daunen<br>Kuschelweiche bio Daunendecke<br>Weiße Feder® für das ganze Jahr<br>in organic Qualität für den</p><div class="price">ab 359,00 € *</div></div>
  <div class="abs card" style="left:320px;top:1010px"><div class="photo" role="img" aria-label="Daunendecke auf Holzboden" style="background:linear-gradient(160deg,#c98a3c,#f0e8d6 50%,#b97a30)"></div><h3>Daunen Ganzjahresdecke</h3><p>Bio Ganzjahresdecke Daunen<br>Kuschelweiche bio Daunendecke<br>Weiße Feder® für das ganze Jahr<br>in organic Qualität für den</p><div class="price">ab 359,00 € *</div></div>
  <div class="abs card" style="left:634px;top:1010px"><div class="photo" role="img" aria-label="Bunte Bettwäsche im Garten" style="background:linear-gradient(180deg,#6f9b5a 0%,#e9b23a 55%,#3b6fb0 100%)"></div><h3>Daunen Ganzjahresdecke</h3><p>Bio Ganzjahresdecke Daunen<br>Kuschelweiche bio Daunendecke<br>Weiße Feder® für das ganze Jahr<br>in organic Qualität für den</p><div class="price">ab 359,00 € *</div></div>

  <div class="abs card" style="left:2px;top:1458px"><div class="photo" role="img" aria-label="Person auf Nackenkissen" style="background:linear-gradient(180deg,#e6b7aa,#efe0c6)"></div><h3>Daunen Ganzjahresdecke</h3><p>Bio Ganzjahresdecke Daunen<br>Kuschelweiche bio Daunendecke<br>Weiße Feder® für das ganze Jahr<br>in organic Qualität für den</p><div class="price">ab 359,00 € *</div></div>
  <div class="abs card" style="left:320px;top:1458px"><div class="photo" role="img" aria-label="Bett mit Decke vor Holzgitter" style="background:linear-gradient(180deg,#8a6a3e,#c2b8b0 60%,#eeeeee)"></div><h3>Daunen Ganzjahresdecke</h3><p>Bio Ganzjahresdecke Daunen<br>Kuschelweiche bio Daunendecke<br>Weiße Feder® für das ganze Jahr<br>in organic Qualität für den</p><div class="price">ab 359,00 € *</div></div>
  <div class="abs card" style="left:634px;top:1458px"><div class="photo" role="img" aria-label="Gestapelte Bettdecken und Kissen" style="background:linear-gradient(180deg,#2b2b2b,#efe9dd 40%,#e4ddcf)"></div><h3>Daunen Ganzjahresdecke</h3><p>Bio Ganzjahresdecke Daunen<br>Kuschelweiche bio Daunendecke<br>Weiße Feder® für das ganze Jahr<br>in organic Qualität für den</p><div class="price">ab 359,00 € *</div></div>

  <div class="abs btn" style="left:287px;top:1928px;width:339px;height:51px">Weitere Artikel laden</div>

  <div class="abs banner photo" role="img" aria-label="Wohnzimmer mit Handwebteppich und Sessel"></div>
  <div class="abs banner-label">Handwebteppiche</div>

  <div class="abs rug" style="left:2px;top:2403px"><div class="photo" role="img" aria-label="Grauer Handwebteppich auf Holzboden" style="background:linear-gradient(160deg,#a9b3b8,#8d989f 60%,#b9783c)"></div><div class="price">ab 112,00 € *</div><h3>Handwebteppich Lorana</h3></div>
  <div class="abs rug" style="left:473px;top:2403px"><div class="photo" role="img" aria-label="Orange und rote Handwebteppiche" style="background:linear-gradient(170deg,#8a6a5a,#e08a5a 50%,#b94a3a)"></div><div class="price">ab 112,00 € *</div><h3>Handwebteppich Mirelo</h3></div>

  <div class="abs teaser" style="top:2870px"><div class="photo" role="img" aria-label="Wärmeauflage für Nacken und Schultern" style="background:linear-gradient(180deg,#e8e8e8 0%,#c9b3a8 55%,#3a6fa0 80%,#c9a070 100%)"></div><h3>VitaWarm® Nackenset</h3><p>VitaWarm® Wärmeauflagen - Nackenset<br>Günstiges Set bei Nackenschmerzen und<br>Verspannungen im Bereich des Nackens und<br>der Schultern. Mit diesem Set erhalten</p><div class="price">84,00 € *</div></div>
  <div class="abs teaser" style="top:3215px"><div class="photo" role="img" aria-label="Halskette aus Tigeraugen-Perlen" style="background:radial-gradient(circle,#8a5a30,#9aa88a 70%)"></div><h3>Tigerauge Halskette</h3><p>Wunderschöne Halskette mit Edelsteinen und<br>Silberperlen. Steine: Tigerauge, Citrin, Pyrit<br>Silberteile, Silberverschluss Länge: ca. 45 cm<br>auf</p><div class="price">115,00 € *</div></div>

  <div class="abs footer">
    <div class="abs brand">
      <div class="brand-name"><i></i>Wendorf</div>
      <div class="brand-sub" style="font-size:22px">NATURVERSAND-ONLINESHOP</div>
    </div>
    <div class="abs social"><span></span><span></span><span class="blue"></span></div>
  </div>
</div>
</body>
</html>
```